Velaski Law Firm
Project: Stationary for Law Firm
Stationary for Law Firm - Law
Stationary for Law Firm
Professional
Tomas Edgar Velaski
Attorney / Abogado
418 W. Brambleton Ave Bldg. 3. Suite 560 Charlotte, NC 28790
info@velaskilawfirm.example
www.velaskilawfirm.example
IMMIGRATION LAW
Logo and "Immigration Law"
Brisko Brisko
velaskilawfirm velaskilawfirm
Please also submit drafts for letterhead and envelopes. Thank you.

```html
<!DOCTYPE html>
<html lang="en">
<head>
<meta charset="utf-8">
<title>Velaski Law Firm – Business Cards</title>
<link href="https://fonts.googleapis.com/css2?family=Cinzel:wght@500&family=Roboto+Condensed:wght@400;700&display=swap" rel="stylesheet">
<style>
  :root {
    --backdrop: #3b3936;
    --card: #ffffff;
    --card-shade: #e9e9ec;
    --navy: #1f2a6b;
    --band: #4b47b3;
    --band-dark: #3a379a;
    --swoosh: #c9c9cf;
    --ink-light: #ffffff;
  }
  * { margin: 0; padding: 0; box-sizing: border-box; }
  html, body { width: 1200px; height: 770px; overflow: hidden; }
  body {
    background: var(--backdrop);
    position: relative;
    font-family: "Roboto Condensed", sans-serif;
  }
  .card {
    position: absolute;
    width: 540px;
    height: 309px;
    border-radius: 14px;
    overflow: hidden;
    background: linear-gradient(180deg, var(--card) 0%, var(--card) 55%, var(--card-shade) 100%);
  }
  .card--back { left: 40px; top: 230px; }
  .card--front { left: 620px; top: 230px; }

  .brand {
    position: absolute;
    left: 0; right: 0;
    display: flex;
    flex-direction: column;
    align-items: center;
    gap: 8px;
  }
  .card--back .brand { top: 92px; }
  .card--front .brand { top: 30px; }
  .brand__square {
    width: 34px; height: 34px;
    background: var(--navy);
  }
  .brand__name {
    font-family: "Cinzel", serif;
    font-weight: 500;
    font-size: 25px;
    letter-spacing: 0.5px;
    color: var(--navy);
    white-space: nowrap;
    line-height: 1.1;
  }
  .brand__name small { font-size: 13px; }
  .brand__tagline {
    font-size: 11px;
    letter-spacing: 3px;
    color: var(--navy);
    text-transform: uppercase;
  }

  .band { position: absolute; inset: 0; }

  .contact {
    position: absolute;
    left: 0; right: 0; top: 196px;
    display: flex;
    justify-content: center;
    color: var(--ink-light);
  }
  .contact__person {
    text-align: right;
    padding-right: 16px;
    border-right: 1px solid rgba(255,255,255,0.8);
    font-size: 10px;
    line-height: 1.45;
    letter-spacing: 0.5px;
  }
  .contact__name { font-size: 13px; font-weight: 700; letter-spacing: 1.1px; text-transform: uppercase; }
  .contact__role { margin-bottom: 5px; }
  .contact__lines {
    list-style: none;
    padding-left: 16px;
    padding-top: 4px;
    font-size: 10.5px;
    letter-spacing: 0.5px;
  }
  .contact__lines li { display: flex; align-items: center; gap: 7px; height: 15px; }
  .contact__lines svg { width: 10px; height: 10px; flex: none; }
</style>
</head>
<body>

  <section class="card card--back" aria-label="Business card back">
    <div class="brand">
      <span class="brand__square"></span>
      <span class="brand__name">VELASKI LAW FIRM, <small>PLLC</small></span>
      <span class="brand__tagline">Immigration Law</span>
    </div>
  </section>

  <section class="card card--front" aria-label="Business card front">
    <svg class="band" viewBox="0 0 540 309" preserveAspectRatio="none" aria-hidden="true">
      <path d="M0 166 Q290 214 540 122 L540 140 Q290 226 0 180 Z" fill="var(--swoosh)"/>
      <path d="M0 178 Q290 226 540 138 L540 309 L0 309 Z" fill="var(--band)"/>
      <path d="M0 290 Q290 300 540 250 L540 309 L0 309 Z" fill="var(--band-dark)" opacity="0.35"/>
    </svg>

    <div class="brand">
      <span class="brand__square"></span>
      <span class="brand__name">VELASKI LAW FIRM, <small>PLLC</small></span>
      <span class="brand__tagline">Immigration Law</span>
    </div>

    <div class="contact">
      <div class="contact__person">
        <p class="contact__name">Tomas Edgar Velaski</p>
        <p class="contact__role">Attorney / Abogado</p>
        <p>418 W. Brambleton Ave</p>
        <p>Bldg. 3. Suite 560</p>
        <p>Charlotte, NC 28790</p>
      </div>
      <ul class="contact__lines">
        <li><svg viewBox="0 0 10 10"><circle cx="5" cy="5" r="5" fill="#fff"/><path d="M3 2.5 L4.3 2.5 L4.6 4 L3.9 4.6 Q4.6 5.7 5.4 6.1 L6 5.4 L7.5 5.7 L7.5 7 Q4 7.5 3 2.5Z" fill="var(--band)"/></svg>704-555-0142</li>
        <li><svg viewBox="0 0 10 10"><circle cx="5" cy="5" r="5" fill="#fff"/><path d="M3 2.5 L4.3 2.5 L4.6 4 L3.9 4.6 Q4.6 5.7 5.4 6.1 L6 5.4 L7.5 5.7 L7.5 7 Q4 7.5 3 2.5Z" fill="var(--band)"/></svg>704-555-0187</li>
        <li><svg viewBox="0 0 10 10"><circle cx="5" cy="5" r="5" fill="#fff"/><path d="M3 2.5 L4.3 2.5 L4.6 4 L3.9 4.6 Q4.6 5.7 5.4 6.1 L6 5.4 L7.5 5.7 L7.5 7 Q4 7.5 3 2.5Z" fill="var(--band)"/></svg>704-555-0163</li>
        <li><svg viewBox="0 0 10 10"><circle cx="5" cy="5" r="5" fill="#fff"/><rect x="2.5" y="3.2" width="5" height="3.6" fill="none" stroke="var(--band)" stroke-width="0.8"/><path d="M2.5 3.2 L5 5.2 L7.5 3.2" fill="none" stroke="var(--band)" stroke-width="0.8"/></svg>info@velaskilawfirm.example</li>
        <li><svg viewBox="0 0 10 10"><circle cx="5" cy="5" r="5" fill="#fff"/><circle cx="5" cy="5" r="2.6" fill="none" stroke="var(--band)" stroke-width="0.8"/><path d="M2.4 5 H7.6 M5 2.4 V7.6" stroke="var(--band)" stroke-width="0.6"/></svg>www.velaskilawfirm.example</li>
      </ul>
    </div>
  </section>

</body>
</html>
```